Vantelle Naturals- An All Natural Hair & Skincare Company needs a website design.

Vantelle Naturals is an all-natural Hair & Skin Company that provides all natural hair and skin care products to the ever growing natural hair community. Our primary target market is African American women between the ages of 16-50. I would like my website to be setup in a way that allows me to add photos, and products for sale easily. The site should be very user friendly but clean and professional looking. I have uploaded our new company Logo and I would definitely like it used throughout the pages. Ideally, the site should display our Motto, Company Vision, Pictures of Products and Results of use of products, testimonials from customers, Video tutorials. I need to be able to capture email addresses for easy email blasts and customer data collection, contact info, links to social media accounts, and detailed analytics to track traffic etc. I also need direct links to my PayPal and email.

It appears my brief is unclear. This is our first site. So i would like it to be able to showcase and all my products. I would like the coding for easy changes after the site goes live. I am not super tech savvy, but would like to be able to add new products and track traffic. Please let me know if this still needs clarification.

Industry/Entity Type

Hair

Coding

Coded - Design and coding required

```html
<!DOCTYPE html>
<html lang="en">
<head>
<meta charset="utf-8">
<title>Vantelle Naturals</title>
<link rel="stylesheet" href="https://fonts.googleapis.com/css2?family=Oswald:wght@400;500&family=Open+Sans:wght@400;600;700&family=Titillium+Web:wght@400;600&family=Pacifico&display=swap">
<style>
:root{
  --orange:#f5891f;
  --orange-dark:#e06f0c;
  --brown:#5d4a42;
  --brown-text:#5a4a42;
  --dark:#140b0f;
  --nav:#1b0e13;
  --magenta:#b8275e;
  --text:#5b5b5b;
  --white:#ffffff;
  --blue:#1ba0d8;
}
*{margin:0;padding:0;box-sizing:border-box}
html,body{width:1200px;height:2699px;overflow:hidden}
body{position:relative;background:var(--white);font-family:"Open Sans",sans-serif;color:var(--text)}
.abs{position:absolute}
.topbar{left:0;top:0;width:1200px;height:7px;background:var(--orange)}
.brand{left:110px;top:30px;width:120px;text-align:center}
.brand-dot{width:70px;height:70px;border-radius:50%;background:var(--brown);margin:0 auto 10px}
.brand-name{font-family:"Titillium Web",sans-serif;font-size:15px;color:var(--brown-text);line-height:1.1}
.contact{left:836px;top:62px;display:flex;gap:16px;align-items:center}
.contact-icon{width:50px;height:50px;border:2px solid var(--orange);border-radius:50%;display:flex;align-items:center;justify-content:center}
.contact-mail{font-size:15px;color:var(--brown-text)}
.contact-phone{font-size:22px;color:var(--orange);margin-top:2px}
.hero{left:0;top:166px;width:1200px;height:502px;background:radial-gradient(ellipse at 60% 40%,#cf3a72 0%,#a82158 55%,#7c1640 100%)}
.hero-figure{left:600px;top:166px;width:330px;height:502px;background:linear-gradient(180deg,#2a1a1a 0%,#6b3a2e 35%,#c9876a 60%,#b85a4e 100%);opacity:.55;border-radius:160px 160px 0 0}
.hero-title{left:113px;top:388px;font-family:Oswald,sans-serif;font-weight:500;font-size:52px;color:var(--white);letter-spacing:1px}
.hero-arrow{top:403px}
.nav{left:0;top:668px;width:1200px;height:73px;background:var(--nav)}
.nav a{position:absolute;top:0;height:73px;line-height:73px;font-family:Oswald,sans-serif;font-size:15px;color:var(--white);text-decoration:none;text-transform:uppercase;transform:translateX(-50%)}
.nav a.active{background:var(--orange);width:131px;text-align:center}
.h2{font-family:"Titillium Web",sans-serif;font-weight:400;color:var(--brown-text)}
.welcome-title{left:113px;top:795px;font-size:35px}
.welcome-title span{color:var(--orange)}
.welcome-copy{left:113px;top:852px;width:580px;font-size:11px;line-height:21.5px}
.btn{display:block;background:linear-gradient(180deg,#f99a2e,var(--orange-dark));color:var(--white);font-size:12px;font-weight:600;text-align:center;border-radius:3px;text-transform:uppercase}
.btn-read{left:113px;top:1007px;width:142px;height:44px;line-height:44px;text-transform:none;font-size:13px}
.board{left:722px;top:840px;width:362px;height:225px;background:#6e3f21;border-radius:4px;box-shadow:0 4px 10px rgba(0,0,0,.3)}
.board-paper{left:737px;top:853px;width:332px;height:199px;background:#f3f1ee}
.board-title{left:737px;top:858px;width:332px;text-align:center;font-family:"Titillium Web",sans-serif;font-size:17px;color:var(--orange)}
.board-list{left:768px;top:893px;width:290px;font-size:11px;color:#333}
.board-list p{height:26px;line-height:26px;border-bottom:1px solid #ddd}
.products-title{left:113px;top:1108px;font-size:33px}
.card{top:1183px;width:310px}
.card-img{width:310px;height:172px;border:4px solid #e5e5e5}
.card-kicker{margin-top:17px;font-family:"Titillium Web",sans-serif;font-weight:600;font-size:17px;color:var(--orange)}
.card-row{display:flex;justify-content:space-between;font-size:16px;color:#222;margin-top:6px}
.card-desc{font-size:11px;line-height:19px;margin-top:8px;width:300px}
.btn-cart{width:125px;height:38px;line-height:38px;margin-top:14px}
.results{left:0;top:1556px;width:1200px;height:469px;background:linear-gradient(90deg,#0b0708 0%,#1a1010 50%,#2a1412 75%,#120a0a 100%)}
.result-img{width:199px;height:160px;border:3px solid #d8d8d8}
.results-title{left:580px;top:1683px;width:500px;text-align:center;font-family:"Titillium Web",sans-serif;font-weight:600;font-size:35px;color:var(--white)}
.results-copy{left:568px;top:1738px;width:524px;text-align:center;font-size:11px;line-height:24px;color:var(--white)}
.btn-results{left:743px;top:1869px;width:125px;height:38px;line-height:38px}
.blog-title{left:113px;top:2048px;font-size:25px}
.post{top:2095px;width:310px}
.post-img{width:310px;height:152px}
.post-meta{font-size:11px;margin-top:18px;color:#555}
.post-head{font-size:12px;font-weight:600;color:#222;margin-top:7px}
.video{left:768px;top:2049px;width:317px;height:251px;background:linear-gradient(180deg,#7b8fa1 0%,#4e5964 60%,#2c2f33 100%)}
.video-title{left:768px;top:2120px;width:317px;text-align:center;font-family:Pacifico,cursive;font-size:32px;color:var(--white)}
.btn-video{left:864px;top:2190px;width:125px;height:36px;line-height:36px}
.footer{left:0;top:2353px;width:1200px;height:231px;background:var(--brown)}
.f-head{font-size:15px;color:var(--white)}
.avatar{left:115px;top:2430px;width:115px;height:115px;border-radius:50%;border:4px solid var(--white);background:linear-gradient(160deg,#6b4634,#2d1b14)}
.quote{left:285px;top:2422px;width:265px;font-size:11px;line-height:19px;color:var(--white)}
.stars{color:#f5c518;font-size:12px;letter-spacing:1px}
.quote-name{font-size:11px;font-weight:700;margin-top:4px}
.social{left:595px;top:2422px;font-size:12px;color:var(--white)}
.social li{list-style:none;height:27px;display:flex;align-items:center;gap:12px}
.social i{display:inline-block;width:8px;height:8px;border-radius:50%;background:var(--white)}
.news-copy{left:853px;top:2422px;width:240px;font-size:12px;line-height:20px;color:var(--white)}
.news-input{left:855px;top:2475px;width:230px;height:33px;background:#9a9696;font-size:10px;color:#eee;padding:11px 10px}
.news-btn{left:855px;top:2516px;width:118px;height:33px;line-height:33px;background:var(--blue);color:var(--white);font-size:11px;text-align:center}
.bottom{left:0;top:2584px;width:1200px;height:115px;background:var(--orange)}
.bottom-links{left:113px;top:2613px;font-size:11px;color:var(--white)}
.copyright{left:113px;top:2642px;font-size:11px;color:var(--white)}
.pay{top:2620px;width:52px;height:36px;background:var(--white);border-radius:3px}
</style>
</head>
<body>
<div class="abs topbar"></div>

<header>
  <div class="abs brand">
    <div class="brand-dot"></div>
    <div class="brand-name">Vantelle Naturals</div>
  </div>
  <div class="abs contact">
    <div class="contact-icon">
      <svg width="22" height="22" viewBox="0 0 24 24"><path d="M6.6 10.8a15 15 0 0 0 6.6 6.6l2.2-2.2c.3-.3.7-.4 1-.2 1.1.4 2.3.6 3.6.6.6 0 1 .4 1 1V20c0 .6-.4 1-1 1A17 17 0 0 1 3 4c0-.6.4-1 1-1h3.5c.6 0 1 .4 1 1 0 1.3.2 2.5.6 3.6.1.3 0 .7-.2 1z" fill="#f5891f"/></svg>
    </div>
    <div>
      <div class="contact-mail">hello@vantellenaturals.com</div>
      <div class="contact-phone">+1 555 0142 2210</div>
    </div>
  </div>
</header>

<section>
  <div class="abs hero" role="img" aria-label="Magenta studio backdrop for the hair and skin slideshow"></div>
  <div class="abs hero-figure" role="img" aria-label="Photo of a woman with a full natural afro and sunglasses"></div>
  <h1 class="abs hero-title">NATURAL HAIR &amp; SKIN</h1>
  <svg class="abs hero-arrow" style="left:44px" width="24" height="36" viewBox="0 0 24 36"><path d="M20 4 6 18l14 14" stroke="#fff" stroke-width="7" fill="none"/></svg>
  <svg class="abs hero-arrow" style="left:1122px" width="24" height="36" viewBox="0 0 24 36"><path d="M4 4l14 14L4 32" stroke="#fff" stroke-width="7" fill="none"/></svg>
</section>

<nav class="abs nav">
  <a class="active" href="#" style="left:180px">Home</a>
  <a href="#" style="left:331px">About Us</a>
  <a href="#" style="left:491px">Gallery</a>
  <a href="#" style="left:638px">Blog</a>
  <a href="#" style="left:803px">Hair Cuttings</a>
  <a href="#" style="left:986px">Contact Us</a>
</nav>

<section>
  <h2 class="abs h2 welcome-title">Welcome To <span>Vantelle</span></h2>
  <p class="abs welcome-copy">Lorem ipsum dolor sit amet, consectetuer adipiscing elit, sed diam nonummy nibh euismod tincidunt ut laoreet dolore magna aliquam erat volutpat. Ut wisi enim ad minim veniam, quis nostrud exerci tation ullamcorper suscipit lobortis nisl ut aliquip ex ea commodo consequat. Lorem ipsum dolor sit amet, consectetuer adipiscing elit, sed diam nonummy nibh euismod tincidunt ut laoreet dolore magna aliquam erat volutpat. Ut wisi enim ad minim veniam, quis nostrud exerci tation ullamcorper suscipit lobortis nisl ut aliquip ex ea commodo consequat.</p>
  <a class="abs btn btn-read" href="#">Read more</a>

  <svg class="abs" style="left:722px;top:770px" width="362" height="80" viewBox="0 0 362 80">
    <path d="M181 18 L30 78 M181 18 L332 78" stroke="#c9a23a" stroke-width="3" fill="none"/>
    <circle cx="181" cy="16" r="11" fill="#bfbfbf"/><circle cx="178" cy="13" r="4" fill="#fff"/>
  </svg>
  <div class="abs board"></div>
  <div class="abs board-paper"></div>
  <div class="abs board-title">Trading Hours</div>
  <div class="abs board-list">
    <p>We are open 7 days</p>
    <p>Monday to Friday 11:30am - 2:30pm</p>
    <p>Saturday to Sunday 11:00am - 3:00pm</p>
    <p>Dinner</p>
    <p>Monday to Friday 11:30am - 2:30pm</p>
    <p>Saturday to Sunday 11:00am - 3:00pm</p>
  </div>
</section>

<section>
  <h2 class="abs h2 products-title">Products</h2>
  <div class="abs card" style="left:113px">
    <div class="card-img" role="img" aria-label="Black and white portrait of a woman with natural hair" style="background:linear-gradient(135deg,#d8d8d8,#6a6a6a)"></div>
    <div class="card-kicker">LOREM IPSUM</div>
    <div class="card-row"><span>$30 1-Hour Massage</span><span>$30.00</span></div>
    <p class="card-desc">Lorem ipsum dolor sit amet, consectetuer adipiscing elit, sed diam nonummy nibh euismod</p>
    <a class="btn btn-cart" href="#">Add Cart</a>
  </div>
  <div class="abs card" style="left:445px">
    <div class="card-img" role="img" aria-label="Woman lying on grass with natural hair spread out" style="background:linear-gradient(135deg,#5a9a4a,#3a2a24 60%,#2a7fbf)"></div>
    <div class="card-kicker">LOREM IPSUM</div>
    <div class="card-row"><span>$40 1-Hour Facial</span><span>$40.00</span></div>
    <p class="card-desc">Lorem ipsum dolor sit amet, consectetuer adipiscing elit, sed diam nonummy nibh euismod</p>
    <a class="btn btn-cart" href="#">Add Cart</a>
  </div>
  <div class="abs card" style="left:776px">
    <div class="card-img" role="img" aria-label="Woman having her curly hair blow-dried in a salon" style="background:linear-gradient(135deg,#e8e4e0,#8a5a40 60%,#d0c8c0)"></div>
    <div class="card-kicker">LOREM IPSUM</div>
    <div class="card-row"><span>$78 Microdermabrasion</span><span>$78.00</span></div>
    <p class="card-desc">Lorem ipsum dolor sit amet, consectetuer adipiscing elit, sed diam nonummy nibh euismod</p>
    <a class="btn btn-cart" href="#">Add Cart</a>
  </div>
</section>

<section>
  <div class="abs results" role="img" aria-label="Dark background photo of a woman in a red scarf"></div>
  <div class="abs result-img" role="img" aria-label="Result photo of a woman with a natural afro on steps" style="left:116px;top:1625px;background:linear-gradient(135deg,#9aa4ad,#3a2a24)"></div>
  <div class="abs result-img" role="img" aria-label="Result photo of a woman with long curly hair" style="left:335px;top:1625px;background:linear-gradient(135deg,#b0b4b8,#2a1c18)"></div>
  <div class="abs result-img" role="img" aria-label="Result photo of a woman with defined curls" style="left:116px;top:1805px;background:linear-gradient(135deg,#e0e0e0,#3a2a24)"></div>
  <div class="abs result-img" role="img" aria-label="Result photo of a smiling woman with voluminous curls" style="left:335px;top:1805px;background:linear-gradient(135deg,#d8d8d8,#5a3a2a)"></div>
  <h2 class="abs results-title">Results</h2>
  <p class="abs results-copy">Lorem ipsum dolor sit amet, consectetuer adipiscing elit, sed diam nonummy nibh euismod tincidunt ut laoreet dolore magna aliquam erat volutpat. Ut wisi enim ad minim veniam, quis nostrud exerci tation ullamcorper suscipit lobortis nisl Lorem ipsum dolor sit amet, consectetuer adipiscing elit, sed diam nonummy nibh euismod tincidunt ut laoreet dolore magna aliquam</p>
  <a class="abs btn btn-results" href="#">Read More</a>
</section>

<section>
  <h2 class="abs h2 blog-title">Latest Blog</h2>
  <article class="abs post" style="left:113px">
    <div class="post-img" role="img" aria-label="Blog photo of a woman with curly hair by a window" style="background:linear-gradient(135deg,#e6e6e6,#4a3028)"></div>
    <div class="post-meta">Aug 9, 2013 &nbsp;3 comments</div>
    <div class="post-head">Lorem ipsum dolor sit amet</div>
  </article>
  <article class="abs post" style="left:440px">
    <div class="post-img" role="img" aria-label="Blog photo of a woman with red curly hair outdoors" style="background:linear-gradient(135deg,#c8ccc0,#8a2a3a)"></div>
    <div class="post-meta">Aug 9, 2013 &nbsp;3 comments</div>
    <div class="post-head">Lorem ipsum dolor sit amet</div>
  </article>
  <div class="abs video" role="img" aria-label="Video tutorial still of a woman by the waterfront"></div>
  <div class="abs video-title">Hair &amp; Beauty</div>
  <a class="abs btn btn-video" href="#">More Videos</a>
</section>

<footer>
  <div class="abs footer"></div>
  <div class="abs f-head" style="left:113px;top:2392px;font-weight:700;font-size:15px">TESTIMONIALS</div>
  <div class="abs avatar" role="img" aria-label="Customer portrait"></div>
  <div class="abs quote">
    <p>&ldquo;&nbsp; Nulla sollicitudin tincidunt dui et egestas. Phasellus non sem tum, ullamcorper vitae, accumsan dui. Duis dignissim condi lorem. Maecenas facilisis ipsum sed ullamcorper vitae,</p>
    <div class="stars">&#9733;&#9733;&#9733;&#9733;&#9733;</div>
    <div class="quote-name">D. HARTWELL, PH.D., &nbsp;&nbsp;&nbsp;&nbsp;&rdquo;</div>
  </div>

  <div class="abs f-head" style="left:595px;top:2390px">Social Media</div>
  <ul class="abs social" style="top:2424px">
    <li><i></i>Friendbook</li>
    <li><i></i>Chirper</li>
    <li><i></i>Circles Plus</li>
    <li><i></i>Tubecast</li>
  </ul>

  <div class="abs f-head" style="left:851px;top:2390px">Subscribete our newsletter</div>
  <p class="abs news-copy">Lorem ipsum dolor sit amet dolor consectetur adipiscing elit.</p>
  <div class="abs news-input">Email</div>
  <div class="abs news-btn">SUBSCRIBE NOW</div>

  <div class="abs bottom"></div>
  <div class="abs bottom-links">Price a Wallet &nbsp;/&nbsp; Get Hologram Sticker &nbsp;/&nbsp; Security &amp; Faq &nbsp;/&nbsp; About &amp; Contact &nbsp;/&nbsp; Open Licence Notes</div>
  <div class="abs copyright">Copyright 2015 Vantelle. All Rights Reserved.</div>
  <div class="abs pay" style="left:855px"></div>
  <div class="abs pay" style="left:914px"></div>
  <div class="abs pay" style="left:973px"></div>
  <div class="abs pay" style="left:1032px"></div>
</footer>
</body>
</html>
```